Home page makeover

Take my existing home page, www.maplecrestharborline.com and redesign layout to look more current considering today's touch design prevalence.
Reuse existing elements or suggest improved ones if available.
I generally have average CSS and HTML skills using div containers, defining lists and using columns to create the code to support the layout.
Updates
Just wanted to send out a quick message to thank all of you for your submissions. Many of you offered nice designs, but unfortunately could only choose one.
Target Market(s)
Generally targeting individuals with some assets for retirement. Basically your average working professional or business owner.
Industry/Entity Type
It Support
Look and feel
Each slider illustrates characteristics of the customer's brand and the style your logo design should communicate.

```html
<!DOCTYPE html>
<html lang="en">
<head>
<meta charset="utf-8">
<title>Maplecrest Harborline – Home</title>
<link href="https://fonts.googleapis.com/css2?family=Jost:wght@400;500;600&family=Arimo:ital,wght@0,400;0,700;1,400&display=swap" rel="stylesheet">
<style>
  :root{
    --green:#9bc93e;
    --green-dark:#2f6b2a;
    --green-ring:#cfe6a4;
    --orange:#ff9a00;
    --grey-btn:#8f8f8f;
    --grey-band:#f2f2f2;
    --grey-text:#a9a9a9;
    --body-text:#555;
    --heading:#222;
    --footer:#2d2d2d;
    --white:#fff;
  }
  *{box-sizing:border-box;margin:0;padding:0}
  html,body{width:767px;height:1200px;overflow:hidden}
  body{position:relative;background:var(--white);font-family:"Arimo",Arial,sans-serif;color:var(--body-text)}
  .abs{position:absolute}

  /* header */
  .site-header{position:absolute;left:0;top:0;width:767px;height:78px}
  .brand{left:96px;top:14px;display:flex;align-items:center;gap:7px}
  .brand-square{width:14px;height:14px;background:var(--green-dark)}
  .brand-name{font-family:"Jost",sans-serif;font-weight:500;font-size:15px;line-height:17px;color:var(--green-dark)}
  .auth-btn{top:10px;height:18px;width:46px;border-radius:2px;color:var(--white);font-size:9px;display:flex;align-items:center;justify-content:center}
  .auth-btn.sign-in{left:574px;background:var(--green)}
  .auth-btn.sign-up{left:625px;background:var(--grey-btn)}
  .main-nav a{position:absolute;top:47px;font-size:10.5px;color:#444;text-decoration:none}

  /* hero */
  .hero{left:0;top:78px;width:767px;height:297px;
    background:linear-gradient(180deg,#cfdbe6 0%,#e4ecef 18%,#8ea7b8 27%,#6f9a3c 38%,#5f9a2a 60%,#7aae34 80%,#6e9a2b 100%)}
  .hero-arrow{top:128px}
  .hero-title{left:0;width:767px;top:135px;text-align:center;color:var(--white);font-family:"Jost",sans-serif;font-weight:600;font-size:21px;letter-spacing:.3px;text-shadow:0 1px 3px rgba(0,0,0,.35)}
  .hero-sub{left:250px;width:267px;top:162px;text-align:center;color:var(--white);font-size:9.5px;line-height:11px;text-shadow:0 1px 2px rgba(0,0,0,.4)}

  /* steps */
  .step{top:401px;width:163px;text-align:center}
  .step-icon{width:75px;height:75px;margin:0 auto;border-radius:50%;background:var(--green);border:3px solid var(--green-ring);display:flex;align-items:center;justify-content:center}
  .step h2{font-family:"Jost",sans-serif;font-weight:400;font-size:14px;color:var(--heading);margin-top:9px;letter-spacing:.3px}
  .step p{font-size:8.3px;line-height:10.5px;color:var(--grey-text);margin-top:4px}

  /* signup band */
  .signup-band{left:0;top:568px;width:767px;height:223px;background:var(--grey-band)}
  .signup{left:124px;top:30px;width:178px;height:163px;background:#c9c9c9}
  .signup-head{height:28px;background:var(--grey-btn);color:var(--white);font-family:"Jost",sans-serif;font-size:14px;display:flex;align-items:center;justify-content:center;letter-spacing:.3px}
  .signup-field{position:absolute;left:11px;width:157px;height:21px;background:var(--white);font-size:10px;color:#999;padding-left:7px;display:flex;align-items:center}
  .signup-btn{position:absolute;left:11px;top:97px;width:157px;height:21px;background:var(--orange);color:var(--white);font-size:10px;display:flex;align-items:center;justify-content:center}
  .signup-perks{position:absolute;left:0;top:126px;width:178px;height:37px;background:var(--green);list-style:none;padding:4px 0 0 11px}
  .signup-perks li{font-size:7.3px;color:var(--white);height:16px;display:flex;align-items:center;gap:5px}
  .video{left:417px;top:30px;width:244px;height:164px;box-shadow:0 1px 4px rgba(0,0,0,.25)}
  .video-frame{width:244px;height:149px;background:linear-gradient(180deg,#c9dbe6 0%,#9ec0d6 30%,#3f77a6 45%,#4f86b0 62%,#7c8c4a 75%,#5a6b2c 100%)}
  .video-controls{width:244px;height:15px;background:linear-gradient(#eee,#cfcfcf)}

  /* features */
  .section-title{left:0;width:767px;text-align:center;font-family:"Jost",sans-serif;font-weight:400;font-size:17px;color:var(--heading);letter-spacing:.4px}
  .feature{width:240px;display:flex;gap:7px}
  .feature-icon{flex:none;width:28px;height:28px;border-radius:50%;background:var(--green);display:flex;align-items:center;justify-content:center;margin-top:0}
  .feature p{font-size:8.3px;line-height:11.6px;color:var(--body-text)}

  /* testimonials */
  .testimonials-band{left:0;top:988px;width:767px;height:163px;background:var(--grey-band)}
  .quote{width:167px;background:var(--white);box-shadow:0 1px 2px rgba(0,0,0,.15);padding:13px 9px 0 9px;font-size:8.3px;line-height:9.6px;font-style:italic;color:#444}
  .quote-tail{position:absolute;left:24px;bottom:-9px}
  .author{font-size:8.3px;color:#111}
  .author span{color:var(--green)}

  /* footer */
  .site-footer{left:0;top:1151px;width:767px;height:49px;background:var(--footer);color:var(--white);text-align:center;font-size:8.3px;padding-top:11px;line-height:14px}
</style>
</head>
<body>

<header class="site-header">
  <div class="abs brand">
    <span class="brand-square"></span>
    <span class="brand-name">Maplecrest<br>Harborline</span>
  </div>
  <a class="abs auth-btn sign-in">Sign In</a>
  <a class="abs auth-btn sign-up">Sign up</a>
  <nav class="main-nav">
    <a style="left:367px">Home</a>
    <a style="left:419px">About us</a>
    <a style="left:483px">Services</a>
    <a style="left:547px">Testimonials</a>
    <a style="left:625px">Contact us</a>
  </nav>
</header>

<section class="abs hero" role="img" aria-label="Photograph of a green hillside village beneath snowy mountains">
  <svg class="abs hero-arrow" style="left:74px" width="24" height="44" viewBox="0 0 24 44"><polyline points="22,1 2,22 22,43" fill="none" stroke="#fff" stroke-width="1.3"/></svg>
  <svg class="abs hero-arrow" style="left:672px" width="24" height="44" viewBox="0 0 24 44"><polyline points="2,1 22,22 2,43" fill="none" stroke="#fff" stroke-width="1.3"/></svg>
  <h1 class="abs hero-title">RETIREMENT PLANS</h1>
  <p class="abs hero-sub">Lorem ipsum dolor sit amet, consectetur adipiscing elit. Etiam ante massa, consectetur vel rhoncus a eget.</p>
</section>

<section class="steps">
  <div class="abs step" style="left:99px">
    <div class="step-icon">
      <svg width="36" height="32" viewBox="0 0 36 32" fill="#fff"><rect x="2" y="2" width="24" height="7" rx="2"/><rect x="2" y="12" width="18" height="7" rx="2"/><rect x="2" y="22" width="16" height="7" rx="2"/><circle cx="26" cy="21" r="6" fill="none" stroke="#fff" stroke-width="2.5"/><line x1="30" y1="25" x2="34" y2="30" stroke="#fff" stroke-width="3"/></svg>
    </div>
    <h2>IDENTIFY</h2>
    <p>Lorem ipsum dolor sit amet, consectetur adipiscing elit. Nullam semper eu diam eget laoreet. Nunc non orci eu augue.</p>
  </div>
  <div class="abs step" style="left:303px">
    <div class="step-icon">
      <svg width="30" height="34" viewBox="0 0 30 34" fill="none" stroke="#fff" stroke-width="2"><path d="M3 2h15l6 6v10"/><path d="M3 2v30h13"/><line x1="7" y1="11" x2="16" y2="11"/><line x1="7" y1="16" x2="14" y2="16"/><line x1="7" y1="21" x2="12" y2="21"/><circle cx="22" cy="25" r="7"/><polyline points="22,21 22,25 25,27"/></svg>
    </div>
    <h2>PLAN</h2>
    <p>Lorem ipsum dolor sit amet, consectetur adipiscing elit. Nullam semper eu diam eget laoreet. Nunc non orci eu augue.</p>
  </div>
  <div class="abs step" style="left:507px">
    <div class="step-icon">
      <svg width="36" height="34" viewBox="0 0 36 34" fill="none" stroke="#fff" stroke-width="2"><path d="M8 10 Q20 -2 32 10 Z" fill="#fff"/><line x1="20" y1="10" x2="14" y2="30"/><circle cx="10" cy="17" r="2.5" fill="#fff"/><path d="M9 20 L15 26 L26 24"/><line x1="4" y1="31" x2="32" y2="31"/></svg>
    </div>
    <h2>RETIRE</h2>
    <p>Lorem ipsum dolor sit amet, consectetur adipiscing elit. Nullam semper eu diam eget laoreet. Nunc non orci eu augue.</p>
  </div>
</section>

<section class="abs signup-band">
  <form class="abs signup">
    <div class="signup-head">SIGN UP</div>
    <div class="signup-field" style="top:40px">Your Name</div>
    <div class="signup-field" style="top:69px">Email Address</div>
    <div class="signup-btn">Sign Up</div>
    <ul class="signup-perks">
      <li><svg width="8" height="7" viewBox="0 0 8 7"><polyline points="1,3.5 3,5.5 7,1" fill="none" stroke="#fff" stroke-width="1.6"/></svg>Only $19.99 For a One Year Membership</li>
      <li><svg width="8" height="7" viewBox="0 0 8 7"><polyline points="1,3.5 3,5.5 7,1" fill="none" stroke="#fff" stroke-width="1.6"/></svg>Only $9.99 Per Year After That</li>
    </ul>
  </form>
  <div class="abs video">
    <div class="video-frame" role="img" aria-label="Video still of two wooden chairs on a grassy cliff facing the sea">
      <svg width="244" height="149" viewBox="0 0 244 149"><circle cx="122" cy="74" r="15" fill="rgba(255,255,255,.15)" stroke="#fff" stroke-width="2"/><polygon points="118,66 118,82 130,74" fill="#fff"/></svg>
    </div>
    <div class="video-controls">
      <svg width="244" height="15" viewBox="0 0 244 15"><polygon points="8,4 8,11 13,7.5" fill="#444"/><rect x="22" y="6" width="122" height="3" rx="1.5" fill="#555"/><rect x="22" y="6" width="60" height="3" rx="1.5" fill="#e0393e"/><circle cx="82" cy="7.5" r="2.5" fill="#eee" stroke="#777" stroke-width=".6"/><text x="150" y="10" font-size="5" fill="#555" font-family="Arimo, sans-serif">3:47 / 9:29</text><polygon points="180,6 182,6 185,4 185,11 182,9 180,9" fill="#444"/><rect x="190" y="6" width="32" height="3" rx="1.5" fill="#555"/><rect x="232" y="4" width="6" height="6" fill="none" stroke="#555" stroke-width="1"/></svg>
    </div>
  </div>
</section>

<h2 class="abs section-title" style="top:812px">FEATURES</h2>
<div class="abs feature" style="left:95px;top:851px">
  <span class="feature-icon"><svg width="14" height="18" viewBox="0 0 14 18"><text x="7" y="15" text-anchor="middle" font-family="Arimo, sans-serif" font-size="17" fill="#fff">$</text></svg></span>
  <p>Identify and project your retirement needs and expectations including basic living expenses, housing costs, recreation, big ticket non-recurring items, medical and nursing home care.</p>
</div>
<div class="abs feature" style="left:407px;top:851px">
  <span class="feature-icon"><svg width="16" height="13" viewBox="0 0 16 13" fill="#fff"><ellipse cx="8" cy="6.5" rx="6.5" ry="5"/><rect x="4" y="10" width="2" height="3"/><rect x="10" y="10" width="2" height="3"/></svg></span>
  <p>Identify and project all your sources of retirement income including retirement savings, other savings, pension plans, Social Security, life insurance and working part-time during retirement for a period of time.</p>
</div>
<div class="abs feature" style="left:95px;top:915px">
  <span class="feature-icon"><svg width="16" height="15" viewBox="0 0 16 15" fill="#fff"><polygon points="8,1 15,7 13,7 13,14 3,14 3,7 1,7"/><rect x="6.5" y="9" width="3" height="5" fill="#9bc93e"/></svg></span>
  <p>Strategize tapping into the equity of your real estate inclu-ding swapping your primary residence for a different home or retirement area, or selling and renting.</p>
</div>
<div class="abs feature" style="left:407px;top:915px">
  <span class="feature-icon"><svg width="16" height="16" viewBox="0 0 16 16" fill="#fff"><path d="M7 15 L7 10 Q2 8 2 2 Q6 4 7 9 Z"/><path d="M9 15 L9 10 Q14 8 14 2 Q10 4 9 9 Z"/></svg></span>
  <p>Save your work so you can return, revisit and edit your retirement plan at a later date.</p>
</div>

<section class="abs testimonials-band">
  <h2 class="abs section-title" style="top:17px">TESTIMONIALS</h2>
  <div class="abs quote" style="left:96px;top:57px;height:45px">This site is a great place to get a handle on your retirement strategy.
    <svg class="quote-tail" width="14" height="10" viewBox="0 0 14 10"><polygon points="0,0 14,0 2,10" fill="#fff"/></svg></div>
  <p class="abs author" style="left:107px;top:117px">Dana, <span>New Jersey</span></p>
  <div class="abs quote" style="left:299px;top:57px;height:53px">It's the only retirement projection tool for the average user that puts it<br>all together.
    <svg class="quote-tail" width="14" height="10" viewBox="0 0 14 10"><polygon points="0,0 14,0 2,10" fill="#fff"/></svg></div>
  <p class="abs author" style="left:310px;top:127px">Owen, <span>New York</span></p>
  <div class="abs quote" style="left:504px;top:57px;height:45px">I can see professionals using this site to validate their existing retirement plans.
    <svg class="quote-tail" width="14" height="10" viewBox="0 0 14 10"><polygon points="0,0 14,0 2,10" fill="#fff"/></svg></div>
  <p class="abs author" style="left:514px;top:117px">Owen, <span>New Jersey</span></p>
</section>

<footer class="abs site-footer">
  Copyright © 2013 Maplecrest Harborline, Inc. All rights reserved.<br>
  Terms and Conditions &nbsp;|&nbsp; Privacy Policy
</footer>

</body>
</html>
```